Zielgruppe
Wir sind ein Vertriebsunternehmen, mit dem Ziel die klassische Finanz und den Kryptosektor zu verbinden. Unsere Zielgruppe sind Menschen zwischn 25 - 45 Jahre. Wir sind die Communty und Vertrieb der ersten rechtkonformen STO - Plattform ( Plattform für Wertpapiere im Kryptosektor)
Diese Projekt ist Teil eines Paketes, wir bitten nur Designer mit zu machen die alle benötigten Unterlagen designen können. (siehe restliche Projekte) - Gesamtvolumen: 2300€ Preisgeld
Online-Marketing Material
2 Vorlagen Social Media - (Einladung/Event, Sprüche/Information)
Banner
Präsentationsvorlagen - min unterschiedliche 8 Vorlagenseiten /Layouts.
Landingpage Layout f. Funnelsite für Webinaranmeldung mit Platz für Formular
Newsletter Layoutvorlage
Vorlage Infografik
Broschüre / E - Book Designe
Es werden nur Vorlagen benötigt mit 'LoremSum Texten' und Musterbildern. Wir möchten von allen Vorlagen die Originaldatei, uns stehen folgende Grafikprogramme zur Verfügung:
Adobe Photoshop
Adobe Illustrator
Canva
Newsletter und Landingpage Software: postwelle.com
Unsere Akt. Designe (Designe Alt) gefällt uns von der Idee, dennoch wünschen wir es uns moderner und edler mit ein wenig 'spaceig'. - Eben die Vereinigung von Kryptowelt und klassischer Finanz.
Schriftart: Poppins
Farben lt. Logo
Aufgabenstellung
Die Landingpage Layout f. Funnelsite für Webinaranmeldung mit Platz für Formular - Die Landingpage ersetzt nicht unsere aktuelle Website - sondern dient zur Leadgenerierung im Socialmedia Bereich.

```html
<!DOCTYPE html>
<html lang="de">
<head>
<meta charset="utf-8">
<title>Scam-Prävention Webinar – GreenMarten Investments</title>
<link rel="stylesheet" href="https://fonts.googleapis.com/css2?family=Poppins:ital,wght@0,300;0,400;0,500;0,600;0,700;1,400&display=swap">
<style>
:root{
  --bg-top:#e9eaf4;
  --bg-mid:#f5f5fa;
  --navy:#1b3f86;
  --blue:#1f4f9e;
  --blue-bright:#2f6ad4;
  --blue-deep:#163a80;
  --ink:#1e2433;
  --muted:#5b6170;
  --card:#eef0f7;
  --slate:#3d4b63;
  --slate-dark:#2d3a50;
  --white:#ffffff;
}
*{box-sizing:border-box;margin:0;padding:0}
html,body{width:1200px;height:3444px;overflow:hidden}
body{
  font-family:'Poppins',sans-serif;color:var(--ink);position:relative;
  background:linear-gradient(180deg,var(--bg-top) 0,var(--bg-mid) 1700px,#f2f2f8 2400px,var(--bg-top) 3340px);
}
.abs{position:absolute}
.divider{display:flex;gap:6px;align-items:center}
.divider span{height:3px;border-radius:2px;background:#9aa4b8}
.divider span.dark{background:var(--slate-dark)}

/* hero */
.hero{left:100px;top:74px;width:1000px;height:504px;border-radius:28px;overflow:hidden;
  background:radial-gradient(circle at 80% 30%,#2a62b8 0,#1e4f9e 45%,#1b4591 100%)}
.hero-photo{position:absolute;left:560px;top:118px;width:500px;height:500px;border-radius:50%;
  background:radial-gradient(circle at 50% 40%,#6f9ee0 0,#3c74c4 55%,#2a5aa8 100%)}
.hero-cut{position:absolute;left:0;top:410px;width:640px;height:94px}
.hero-brand{left:183px;top:150px;color:#fff;font-size:17px;font-weight:400;letter-spacing:.2px}
.hero-title{left:183px;top:178px;color:#fff;font-size:40px;line-height:47px;font-weight:700}
.hero-date{left:183px;top:319px;color:#fff;font-size:40px;line-height:47px;font-weight:400}
.hero-cta{left:183px;top:512px;font-size:25px;font-weight:500;color:var(--ink);display:flex;align-items:center;gap:18px}
.hero-cta .arrow{width:42px;height:42px;border-radius:50%;background:linear-gradient(135deg,#3d7ae0,#1f4f9e);display:flex;align-items:center;justify-content:center}
.brand-badge{left:510px;top:18px;width:180px;height:180px;border-radius:50%;background:var(--bg-top);
  display:flex;flex-direction:column;align-items:center;justify-content:center;gap:8px}
.brand-badge .dot{width:70px;height:70px;border-radius:50%;background:var(--blue)}
.brand-badge .name{font-size:15px;font-weight:600;color:var(--blue)}

/* intro */
.intro-title{left:150px;top:660px;width:900px;text-align:center;color:var(--blue);font-size:38px;line-height:45px;font-weight:600}
.intro-divider{left:537px;top:812px}
.intro-text{left:120px;top:844px;width:960px;text-align:center;font-size:11.5px;line-height:22px;color:var(--muted)}

/* contents */
.contents-title{left:107px;top:968px;color:var(--blue);font-size:38px;line-height:45px;font-weight:600}
.contents-divider{left:107px;top:1065px}
.topic{width:313px;border-radius:8px;background:linear-gradient(180deg,#f2f3f9,#e5e7f1);
  box-shadow:0 6px 14px rgba(40,60,110,.12);padding:14px 14px 14px 70px;font-size:12px;line-height:17.5px;color:var(--muted)}
.topic h3{font-size:12.5px;font-weight:500;color:var(--ink);line-height:17.5px;margin-bottom:1px}
.topic ul{list-style:none}
.topic li{position:relative;padding-left:15px}
.topic li::before{content:"";position:absolute;left:1px;top:4px;width:8px;height:5px;border-left:2px solid var(--blue-bright);border-bottom:2px solid var(--blue-bright);transform:rotate(-45deg)}
.topic .icon{position:absolute;left:14px;top:14px;width:44px;height:44px;border-radius:50%;
  background:linear-gradient(135deg,#4b86e6,#1f4f9e);display:flex;align-items:center;justify-content:center;box-shadow:0 0 0 3px #c9d3ea}

/* banner */
.banner{left:100px;top:1446px;width:1000px;height:257px;border-radius:24px;
  background:linear-gradient(100deg,#3a6fd0 0,#2d63cc 55%,#2a5fc6 100%);box-shadow:0 10px 24px rgba(40,80,170,.25);overflow:hidden}
.banner-photo{position:absolute;left:70px;top:14px;width:210px;height:243px;border-radius:100px 100px 0 0;
  background:linear-gradient(180deg,#e9e2da 0,#d3d6df 55%,#b9bfcb 100%)}
.banner-title{left:410px;top:1484px;color:#fff;font-size:32px;line-height:38px;font-weight:600;width:640px}
.banner-text{left:410px;top:1564px;color:#fff;font-size:15px;line-height:22px;width:660px}
.btn-dark{left:410px;top:1623px;width:151px;height:36px;border-radius:6px;background:linear-gradient(180deg,#4a5a74,#2e3a4f);
  color:#fff;font-size:12.5px;display:flex;align-items:center;justify-content:center}

/* target group */
.target-title{left:100px;top:1815px;color:var(--blue);font-size:38px;font-weight:600;line-height:45px}
.target-divider{left:100px;top:1876px}
.target-text{left:100px;top:1890px;width:620px;font-size:12px;line-height:22.5px;color:var(--muted)}
.target-photo{left:769px;top:1790px;width:331px;height:216px;border-radius:4px;
  background:linear-gradient(135deg,#3c3f46 0,#6a6b6f 45%,#c7c4bf 75%,#e9e6e1 100%);box-shadow:0 6px 14px rgba(0,0,0,.15)}

/* speaker */
.speaker-box{left:100px;top:2107px;width:331px;height:174px;border-radius:4px;
  background:linear-gradient(135deg,#6f86a8,#3e5880);box-shadow:0 6px 14px rgba(0,0,0,.15)}
.speaker-deco{left:265px;top:2092px;width:165px;height:205px;border-radius:30px;background:linear-gradient(160deg,#5a8fe0,#1f4f9e)}
.speaker-photo{left:122px;top:2134px;width:121px;height:123px;border-radius:6px;background:linear-gradient(180deg,#7a9a6e,#3b4b3a 60%,#2a2e38)}
.speaker-title{left:503px;top:2132px;color:var(--blue);font-size:38px;font-weight:600;line-height:45px}
.speaker-divider{left:503px;top:2193px}
.speaker-text{left:503px;top:2209px;width:580px;font-size:11px;line-height:22px;color:var(--muted)}
.speaker-text b{font-size:14px;font-weight:500;color:var(--ink)}

/* testimonial */
.quote-box{left:100px;top:2384px;width:1000px;height:176px;border-radius:6px;background:linear-gradient(180deg,#e7e9f2,#eef0f6);box-shadow:0 6px 14px rgba(40,60,110,.12)}
.quote-pointer{left:580px;top:2558px;width:0;height:0;border-left:20px solid transparent;border-right:20px solid transparent;border-top:20px solid #eef0f6}
.quote-mark{left:112px;top:2380px;font-size:150px;line-height:150px;font-weight:700;color:#cfd2db;font-family:Georgia,serif}
.quote-text{left:140px;top:2412px;width:920px;text-align:center;font-style:italic;font-size:12px;line-height:23.3px;color:var(--muted)}
.avatar{border-radius:50%;border:3px solid #3b4659;background:linear-gradient(180deg,#9aa6bb,#5a6780)}
.avatar.active{border-color:var(--blue-bright);background:linear-gradient(180deg,#6a86c6,#2f4f94)}
.nav{color:var(--blue-bright)}
.person-name{left:500px;top:2708px;width:200px;text-align:center;color:var(--blue);font-size:13px;font-weight:600}
.person-role{left:500px;top:2730px;width:200px;text-align:center;color:var(--muted);font-size:11px}

/* form */
.event-card{left:100px;top:2830px;width:323px;height:194px;border-radius:4px;background:linear-gradient(180deg,#f3f4f9,#e8eaf2);box-shadow:0 6px 14px rgba(40,60,110,.12)}
.event-title{left:128px;top:2850px;color:var(--blue);font-size:38px;line-height:45px;font-weight:600}
.event-date{left:107px;top:2953px;width:309px;height:63px;background:#dcdfea;border-radius:3px;display:flex;align-items:center;padding-left:21px;font-size:14px;font-weight:500}
.form-panel{left:446px;top:2830px;width:654px;height:341px;border-radius:6px;background:linear-gradient(180deg,#3e5573,#2c3a50)}
.field{border-radius:4px;background:linear-gradient(180deg,#f2f3f7,#fff);color:#b3b8c4;font-size:15px;display:flex;align-items:center;padding-left:23px}
.check{left:466px;width:610px;display:flex;gap:10px;color:#fff;font-size:11.5px;line-height:22px}
.check .box{flex:none;width:16px;height:16px;border-radius:3px;background:#fff;margin-top:3px}
.check u{text-underline-offset:3px}
.submit{left:446px;top:3190px;width:654px;height:64px;border-radius:6px;background:linear-gradient(180deg,#3470d8,#1f4fa8);
  color:#fff;font-size:20px;letter-spacing:.5px;display:flex;align-items:center;justify-content:center;box-shadow:0 6px 14px rgba(30,70,160,.25)}

/* footer */
.footer{left:0;top:3342px;width:1200px;height:102px;background:var(--blue-deep)}
.footer-brand{left:100px;top:3360px;width:318px;height:69px;border-radius:6px;background:#fff;padding:10px 20px}
.footer-brand .row{display:flex;align-items:center;gap:8px}
.footer-brand .sq{width:20px;height:20px;background:var(--blue);border-radius:3px}
.footer-brand .name{font-size:15px;font-weight:600;color:var(--blue);letter-spacing:.3px}
.footer-brand .tag{font-size:8.5px;color:var(--blue);letter-spacing:1.5px;margin-left:28px;line-height:10px}
.footer-brand .copy{font-size:9px;color:var(--blue);margin-top:6px}
.footer-links{right:100px;top:3386px;color:#fff;font-size:11.5px}
</style>
</head>
<body>

<!-- hero -->
<section class="abs hero">
  <div class="hero-photo" role="img" aria-label="Foto: lächelnder Mann mit Laptop vor hexagonalem Weltraum-Hintergrund"></div>
  <svg class="hero-cut" viewBox="0 0 640 94" preserveAspectRatio="none"><path d="M0 0 H420 C480 0 500 94 640 94 H0 Z" fill="#fff"/></svg>
</section>
<div class="abs brand-badge"><div class="dot"></div><div class="name">GreenMarten</div></div>
<div class="abs hero-brand">GREENMARTEN INVESTMENTS</div>
<h1 class="abs hero-title">Scam -<br>Prävention<br>Webinar</h1>
<div class="abs hero-date">DO. 27.7.2023<br>20:30 Uhr</div>
<div class="abs hero-cta">Jetzt teilnehmen <span class="arrow"><svg width="16" height="16" viewBox="0 0 16 16"><path d="M5 2 L11 8 L5 14" stroke="#fff" stroke-width="2.4" fill="none" stroke-linecap="round"/></svg></span></div>

<!-- intro -->
<h2 class="abs intro-title">Scam oder seriös? Erkennst DU betrügerische Projekte und legale Chancen mit hohem Gewinnpotenzial?</h2>
<div class="abs divider intro-divider"><span style="width:10px"></span><span style="width:22px" class="dark"></span><span style="width:50px" class="dark"></span><span style="width:22px"></span><span style="width:10px"></span></div>
<p class="abs intro-text">In unserem interaktiven Webinar "Scam oder seriös?" erfährst DU alles Wichtige zum Thema Scam und wie DU betrügerische Projekte erkennen kannst.<br>Wir klären gemeinsam den Unterschied zwischen einem Scam und einem "nicht rechtskonformen Projekt" und wer darüber entscheidet.</p>

<!-- contents -->
<h2 class="abs contents-title">Inhalt des<br>Webinars:</h2>
<div class="abs divider contents-divider"><span style="width:50px" class="dark"></span><span style="width:22px"></span><span style="width:10px"></span></div>

<article class="abs topic" style="left:447px;top:973px;height:162px">
  <span class="icon"><svg width="20" height="20" viewBox="0 0 20 20"><rect x="3" y="4" width="14" height="10" rx="1" fill="none" stroke="#fff" stroke-width="2"/><path d="M7 17h6" stroke="#fff" stroke-width="2"/></svg></span>
  <h3>Was ist ein Scam?</h3>
  <ul><li>Wir erklären, was ein Scam ist und wie Betrüger diese Maschen nutzen, um Dich und andere Menschen zu täuschen.</li><li>Du erhältst Einblicke in verschiedene Arten von Scams, die in der digitalen Welt verbreitet sind.</li></ul>
</article>
<article class="abs topic" style="left:787px;top:973px;height:162px">
  <span class="icon"><svg width="20" height="20" viewBox="0 0 20 20"><circle cx="10" cy="10" r="8" fill="none" stroke="#fff" stroke-width="2"/><path d="M10 5v7M10 14v1.5" stroke="#fff" stroke-width="2"/></svg></span>
  <h3>Scam erkennen:</h3>
  <ul><li>Erfahre die typischen Merkmale und Warnzeichen eines Scams.</li><li>Erhalte praktische Tipps, wie DU Dich vor betrügerischen Projekten schützen kannst.</li></ul>
</article>
<article class="abs topic" style="left:107px;top:1161px;height:199px">
  <span class="icon"><svg width="20" height="20" viewBox="0 0 20 20"><rect x="3" y="3" width="14" height="14" rx="2" fill="none" stroke="#fff" stroke-width="2"/><path d="M8 8a2 2 0 1 1 2 2v2M10 14v1" stroke="#fff" stroke-width="1.8" fill="none"/></svg></span>
  <h3>Der Unterschied zwischen einem Scam und einem "nicht rechts-konformen Projekt":</h3>
  <ul><li>Wir klären die Abgrenzung zwischen betrügerischen Vorhaben und Projekten, die zwar nicht rechts-konform, aber nicht zwangsläufig betrügerisch sind.</li><li>und warum auch diese genauso schädigen können.</li></ul>
</article>
<article class="abs topic" style="left:447px;top:1161px;height:199px">
  <span class="icon"><svg width="20" height="20" viewBox="0 0 20 20"><rect x="3" y="4" width="14" height="10" rx="1" fill="none" stroke="#fff" stroke-width="2"/><path d="M6 9l2 2 4-4" stroke="#fff" stroke-width="1.8" fill="none"/></svg></span>
  <h3>Zuständigkeiten und Entscheidungen:</h3>
  <ul><li>Finde heraus, wer darüber entscheidet, ob ein Projekt ein Scam ist oder nicht rechtskonform agiert.</li></ul>
</article>
<article class="abs topic" style="left:787px;top:1161px;height:199px">
  <span class="icon"><svg width="20" height="20" viewBox="0 0 20 20"><path d="M3 4h14M6 4v12M10 4v12M14 4v12" stroke="#fff" stroke-width="2"/></svg></span>
  <h3>Auswirkungen und rechtliche Konsequenzen:</h3>
  <ul><li>Erfahre die möglichen Folgen und rechtliche Konsequenzen, die ein Scam auf Dich als Teilnehmer oder Vermittler haben kann.</li></ul>
</article>

<!-- banner -->
<section class="abs banner"><div class="banner-photo" role="img" aria-label="Foto: lächelnder Mann hält einen Laptop"></div></section>
<h2 class="abs banner-title">Rechtskonforme Projekte mit hohem Gewinnpotenzial:</h2>
<p class="abs banner-text">Ja, sie existieren! Wir zeigen Dir, wie Du seriöse Projekte mit hohem Gewinnpotenzial erkennst und von legalen Chancen profitieren kannst.</p>
<div class="abs btn-dark">Jetzt anmelden</div>

<!-- target group -->
<h2 class="abs target-title">Zielgruppe:</h2>
<div class="abs divider target-divider"><span style="width:50px" class="dark"></span><span style="width:22px"></span><span style="width:10px"></span></div>
<p class="abs target-text">Unser Webinar richtet sich an Dich und alle, die sich vor betrügerischen Machenschaften schützen<br>möchten und ihr Wissen über rechtskonforme Projekte mit Gewinnpotenzial erweitern wollen.<br>Egal, ob Du bereits Erfahrungen gesammelt hast oder Dich gerade erst mit dem Thema vertraut machst -<br>wir heißen Dich herzlich willkommen!</p>
<div class="abs target-photo" role="img" aria-label="Foto: Laptop mit Videokonferenz, Tasse und Notizbuch auf einem Schreibtisch"></div>

<!-- speaker -->
<div class="abs speaker-box"></div>
<div class="abs speaker-deco"></div>
<div class="abs speaker-photo" role="img" aria-label="Foto: Referent im Anzug im Garten"></div>
<h2 class="abs speaker-title">Referent:</h2>
<div class="abs divider speaker-divider"><span style="width:50px" class="dark"></span><span style="width:22px"></span><span style="width:10px"></span></div>
<p class="abs speaker-text">Unser Experte, <b>Lukas Fernbach</b>, <b>staatlich geprüfter Vermögensberater</b>, &nbsp;<b>Trader</b> und<br><b>Inhaber</b> der <b>GreenMarten Investments GmbH</b></p>

<!-- testimonial -->
<div class="abs quote-box"></div>
<div class="abs quote-pointer"></div>
<div class="abs quote-mark">“</div>
<p class="abs quote-text">“Muster Testimonial text Lorem ipsum dolor sit amet, consetetur sadipscing elitr, sed diam nonumy eirmod tempor invidunt ut labore et dolore magna aliquyam erat, sed diam voluptua. At vero eos et accusam et justo duo dolores et ea rebum. Stet clita kasd gubergren, no sea takimata sanctus est Lorem ipsum dolor sit amet. Lorem ipsum dolor sit amet tempor invidunt ut labore et dolore magna aliquyam erat.<br>Sed diam voluptua. At vero eos et accusam et justo duo dolores et ea rebum. Stet clita kasd gubergren, no sea takimata sanctus Lorem ipsum dolor sit amet consetetur sadipscing elitr, sed diam nonumy eirmod tempor invidunt ut labore et dolore magna aliquyam erat.”</p>

<svg class="abs nav" style="left:326px;top:2643px" width="20" height="24" viewBox="0 0 20 24"><path d="M14 3 L5 12 L14 21" stroke="currentColor" stroke-width="3" fill="none" stroke-linecap="round"/></svg>
<svg class="abs nav" style="left:853px;top:2643px" width="20" height="24" viewBox="0 0 20 24"><path d="M6 3 L15 12 L6 21" stroke="currentColor" stroke-width="3" fill="none" stroke-linecap="round"/></svg>
<div class="abs avatar" role="img" aria-label="Porträtfoto Teilnehmerin" style="left:383px;top:2626px;width:58px;height:58px"></div>
<div class="abs avatar" role="img" aria-label="Porträtfoto Teilnehmer" style="left:461px;top:2620px;width:70px;height:70px"></div>
<div class="abs avatar active" role="img" aria-label="Porträtfoto Sarah Musterfrau" style="left:553px;top:2608px;width:94px;height:94px"></div>
<div class="abs avatar" role="img" aria-label="Porträtfoto Teilnehmerin" style="left:666px;top:2620px;width:70px;height:70px"></div>
<div class="abs avatar" role="img" aria-label="Porträtfoto Teilnehmer" style="left:756px;top:2626px;width:58px;height:58px"></div>
<div class="abs person-name">Sarah Musterfrau</div>
<div class="abs person-role">Muster Titel</div>

<!-- registration -->
<div class="abs event-card"></div>
<h2 class="abs event-title">Scam<br>Prävention</h2>
<div class="abs event-date">2023-07-27 - 20:30 - Europe/Vienna</div>

<form class="abs form-panel"></form>
<div class="abs field" style="left:466px;top:2851px;width:290px;height:66px">Ihr Name</div>
<div class="abs field" style="left:789px;top:2851px;width:289px;height:66px">Ihre E-Mail</div>
<div class="abs field" style="left:466px;top:2949px;width:612px;height:65px">Telefonnummer</div>
<div class="abs check" style="top:3045px"><span class="box"></span><span>Ja, ich möchte regelmässig von GreenMarten Investments GmbH über Neuigkeiten und Entwicklungen informiert werden.</span></div>
<div class="abs check" style="top:3110px"><span class="box"></span><span>Mit der Anmeldung und Teilnahme an der Veranstaltung / Webinar bestätige ich die <u>Datenschutzrichtlinien und ABG gelesen zu und akzeptiert zu haben.</u></span></div>
<div class="abs submit">Jetzt anmelden</div>

<!-- footer -->
<footer class="abs footer"></footer>
<div class="abs footer-brand">
  <div class="row"><span class="sq"></span><span class="name">GREENMARTEN INVESTMENTS</span></div>
  <div class="tag">EINFACH SMART IN UNTERNEHMEN INVESTIEREN</div>
  <div class="copy">© 2023 GreenMarten Investments. Alle Rechte vorbehalten</div>
</div>
<div class="abs footer-links">AGB | Datenschutz | Impressum | Kontakt</div>

</body>
</html>
```